Landing Page Sicherheitsdruckerei und Aktenvernichtung
Zielgruppe
Sicherheitsdruckerei und Aktenvernichtung
Aufgabenstellung
Technische Vorgaben:
- Umsetzbarkeit auf Shopware-5-System, wenn möglich ohne zusätzliche Plugins
- Sauberer CSS- und HTML-Code mit Kommentaren
Allgemeine Vorgaben:
- Nutzung unserer Hausschriftart (Brandon Grotesque)
- Anlehnung an unsere Webpräsenzen
- Gültige Nutzungsrechte für alle Elemente (Schrift, Grafiken, etc.) zur kommerziellen Verwendung im Web und allgemein
Hinweis: Aktuell ist unser Shop in einer Umstellungsphase, weshalb der neue Shopware-Shop noch nicht erreichbar ist. Im Design ist er aber an den alten Shop bzw. die Homepage angelehnt.
Inhalte, welche auf der Landingpage angezeigt werden sollen, sind im angehängten PDF zu finden.

```html
<!DOCTYPE html>
<html lang="de">
<head>
<meta charset="utf-8">
<title>Wenzlick – Aktenvernichtung</title>
<link href="https://fonts.googleapis.com/css2?family=Jost:wght@400;500;600&display=swap" rel="stylesheet">
<style>
:root{
  --bg:#bfe3de;
  --teal:#8ccfc6;
  --teal-deep:#6fada5;
  --teal-text:#79b6ae;
  --offers:#acdcd6;
  --dark:#333333;
  --grey:#f4f4f4;
  --cell:#ebf5f3;
  --cell-strong:#c2e5e0;
  --ink:#222222;
  --white:#ffffff;
}
*{margin:0;padding:0;box-sizing:border-box}
html,body{width:719px;height:1200px;overflow:hidden}
body{background:var(--bg);font-family:"Jost",sans-serif;color:var(--ink);position:relative}
.abs{position:absolute}
.logo{left:150px;top:33px;font-size:15px;letter-spacing:2.5px;font-weight:400;display:flex;align-items:center;gap:4px}
.logo .dot{width:6px;height:6px;border-radius:50%;background:var(--ink)}
.tagline{left:359px;top:34px;font-size:5px;font-weight:600;letter-spacing:.2px}
.topnav{left:479px;top:34px;font-size:5px;color:var(--teal-text);font-weight:500;display:flex;gap:4px}
.sidenav{left:150px;top:102px;list-style:none;color:var(--white);font-size:7.6px;font-weight:500;line-height:12.4px;letter-spacing:.3px}
.tile{position:absolute}
.facet{left:247px;top:86px;width:113px;height:112px;background:linear-gradient(135deg,#9ad6ce,#82c9c0 60%,#94d3cb)}
.facet .mark{position:absolute;left:50px;top:48px;width:12px;height:12px;border:2.4px solid var(--white);border-radius:50%}
.photo{left:360px;top:86px;width:224px;height:225px;background:linear-gradient(160deg,#e6e8ea,#b9bcc0 45%,#8b8f94)}
.claim{left:472px;top:198px;width:112px;height:113px;background:rgba(51,51,51,.9);color:var(--white);padding:16px 15px;font-size:8px;font-weight:500;line-height:12px}
.arrows{position:absolute;left:71px;top:84px;display:flex;gap:8px}
.blank{left:135px;top:198px;width:112px;height:113px;background:var(--white)}
.intro{left:247px;top:198px;width:113px;height:113px;background:var(--grey);padding:18px 15px}
.intro h3{font-size:5.6px;color:var(--teal-text);font-weight:500;line-height:7.7px;margin-bottom:7px}
.intro p{font-size:5.2px;line-height:7.8px;margin-bottom:7px}
.more{font-size:5.4px;font-weight:600}
.about{left:135px;top:311px;width:225px;height:112px;background:var(--grey);padding:14px 15px}
.about h2{font-size:8px;font-weight:500;margin-bottom:8px}
.about p{font-size:5.1px;line-height:7.8px;margin-bottom:7.5px}
.about .strong{font-weight:600}
.since{left:360px;top:311px;width:112px;height:112px;background:var(--dark);color:var(--white);padding:16px 15px}
.since h3{font-size:8px;font-weight:500;line-height:11.8px;margin-bottom:10px}
.since span{font-size:5.4px;color:var(--teal);font-weight:500}
.compare{left:135px;top:423px;width:337px;height:337px;background:var(--white)}
.plans{position:absolute;left:15px;top:16px;width:306px;border-collapse:collapse;font-size:5.3px;text-align:center;line-height:7.8px}
.plans th{height:27px;font-size:7px;font-weight:500;color:var(--teal-text);background:#cbe9e4}
.plans th+th{border-left:1px solid var(--white)}
.plans th.top{background:var(--dark);color:var(--white)}
.plans td{background:var(--cell);border-top:1px solid var(--white);padding:0 8px}
.plans td+td{border-left:1px solid var(--white)}
.plans td.top{background:var(--cell-strong);box-shadow:2px 0 4px rgba(0,0,0,.06)}
.crown{position:absolute;left:297px;top:5px;width:19px;height:19px;border-radius:50%;background:var(--teal-deep);border:1.5px solid var(--white);display:flex;align-items:center;justify-content:center}
.products{left:472px;top:423px;width:112px;height:112px;background:var(--grey);padding:16px 15px}
.products h2{font-size:8px;font-weight:500;margin-bottom:6px}
.products p{font-size:5.2px;line-height:7.8px;margin-bottom:6px}
.box-photo{left:472px;top:535px;width:112px;height:113px;background:linear-gradient(180deg,#ffffff,#dcdfe1 55%,#f4f5f6)}
.seal{left:472px;top:648px;width:112px;height:112px;background:linear-gradient(135deg,#92d2c9,#84cac1)}
.seal .badge{position:absolute;left:31px;top:28px;width:50px;height:50px;border-radius:6px;background:var(--ink)}
.offers{left:135px;top:760px;width:449px;height:224px;background:var(--offers)}
.offers h2{position:absolute;top:14px;width:100%;text-align:center;font-size:8px;font-weight:500}
.card{position:absolute;top:32px;width:97px;height:165px;background:var(--white);text-align:center}
.card .shot{height:99px;background:linear-gradient(180deg,#ffffff,#d6d9dc 60%,#eef0f1)}
.card h4{font-size:6px;font-weight:600;margin-top:14px}
.card .price{font-size:6px;margin-top:3px}
.card .btn{display:inline-block;margin-top:8px;width:48px;height:12px;line-height:12px;background:var(--teal-deep);color:var(--white);font-size:4.8px;font-weight:600}
.card.hover{box-shadow:0 3px 8px rgba(0,0,0,.1)}
.dots{position:absolute;top:210px;left:210px;display:flex;gap:2px}
.dots i{width:4.5px;height:4.5px;background:#d4ede9}
.dots i:first-child{background:var(--white)}
.cta{top:1028px;width:112px;height:45px;border:6px solid var(--teal-deep);display:flex;align-items:center;justify-content:center;font-size:8.4px;font-weight:500;letter-spacing:.3px}
.cta.contact{border-color:var(--teal)}
.foot-logo{left:135px;top:1143px;font-size:8.5px;letter-spacing:1.6px;display:flex;align-items:center;gap:3px}
.foot-logo .dot{width:4px;height:4px;border-radius:50%;background:var(--ink)}
.foot-mark{left:353px;top:1137px;width:14px;height:14px;border:2.5px solid var(--white);border-radius:50%}
.foot-legal{left:424px;top:1138px;font-size:5.4px;line-height:8px;font-weight:600}
.foot-legal span{font-weight:400}
.up{left:572px;top:1122px}
</style>
</head>
<body>
<div class="abs logo"><span>WENZLICK</span><span class="dot"></span></div>
<div class="abs tagline">AKTENVERNICHTUNG. SICHER. PRÄZISE.</div>
<nav class="abs topnav"><span>ÜBER UNS</span><span>ONLINESHOP</span><span>KONTAKT</span></nav>

<ul class="abs sidenav">
  <li>AKTENVERNICHTUNG</li><li>PRODUKTE</li><li>REFERENZEN</li><li>AKTUELLES</li><li>ONLINESHOP</li><li>KONTAKT</li>
</ul>

<div class="tile facet" role="img" aria-label="Facettiertes Flächenmuster in Türkis"><span class="mark"></span></div>
<div class="tile photo" role="img" aria-label="Foto von geschreddertem Papier und einem Aktenstapel"></div>
<div class="tile claim">MODERNSTE<br>TECHNIK.<br>MAXIMALE<br>SICHERHEIT.
  <div class="arrows">
    <svg width="8" height="10" viewBox="0 0 8 10"><path d="M6 1 2 5l4 4" stroke="#ccc" stroke-width="2" fill="none"/></svg>
    <svg width="8" height="10" viewBox="0 0 8 10"><path d="M2 1l4 4-4 4" stroke="#ccc" stroke-width="2" fill="none"/></svg>
  </div>
</div>

<div class="tile blank"></div>
<div class="tile intro">
  <h3>DATENSCHUTZKONFORME<br>AKTENVERNICHTUNG<br>NACH DSGVO</h3>
  <p>Lorem ipsum dolor sit amet consectetuer Cum sociis nato que penatibus et magnis dis parturient montes ridiculmus.</p>
  <div class="more">Mehr erfahren</div>
</div>

<div class="tile about">
  <h2>AKTENVERNICHTUNG. SICHER. PRÄZISE.</h2>
  <p>Über unseren Onlineshop können sie ganz einfach mit wenigen Klicks die gesetzeskonforme Vernichtung all Ihrer Dokumente und Unterlagen beauftragen. So regeln Sie ein wichtiges Sicherheitsthema schnell und unkompliziert.</p>
  <p>Wir garantieren attraktive Preise für Ihren bestmöglichen Datenschutz. Hierfür bieten wir Ihnen maximale Sicherheit, Planbarkeit und Transparenz.</p>
  <p class="strong">Wir freuen uns, Ihnen den für Sie besten Service anbieten zu können!</p>
</div>
<div class="tile since">
  <h3>SEIT 1893<br>STEHT DER NAME<br>WENZLICK FÜR<br>HÖCHSTE QUALITÄT</h3>
  <span>Made in Germany</span>
</div>

<section class="tile compare">
  <table class="plans">
    <tr><th>Standard-Schutz</th><th>Extra-Schutz</th><th class="top">Absoluter Schutz</th></tr>
    <tr style="height:40px"><td>Schutzklasse 2 /<br>Sicherheitsstufe P3<br>gemäß DIN 66399</td><td>Schutzklasse 3 /<br>Sicherheitsstufe P5<br>gemäß DIN 66399</td><td class="top">Schutzklasse 3 /<br>Sicherheitsstufe P7<br>gemäß DIN 66399</td></tr>
    <tr style="height:40px"><td></td><td>Flexibel monatlich mieten</td><td class="top">Für Berufsgeheimnisträger, Steuerberater, Rechtsanwälte, Ärzte und Notare</td></tr>
    <tr style="height:32px"><td>Stationäre Akten- und Datenvernichtung</td><td>Stationäre Akten- und Datenvernichtung</td><td class="top">Stationäre Akten- und Datenvernichtung</td></tr>
    <tr style="height:40px"><td>Einwurfschlitz oder Ordnereinwurf mit Sicherheitsschloss</td><td>Einwurfschlitz oder Ordnereinwurf mit Sicherheitsschloss</td><td class="top">Elektronisches Sicherheitsschloss der Firma Riegeltec mit Zahlencode und RFID-Karte</td></tr>
    <tr style="height:32px"><td>Datenvernichtung inklusive Zertifikat</td><td>Datenvernichtung innerhalb 72 Stunden inklusive Zertifikat</td><td class="top">Datenvernichtung binnen 24 Stunden inklusive Zertifikat</td></tr>
    <tr style="height:32px"><td></td><td></td><td class="top">Dokumentierte Behälteröffnung mit Protokoll</td></tr>
    <tr style="height:32px"><td></td><td></td><td class="top">Videosequenz Ihrer Aktenvernichtung</td></tr>
    <tr style="height:32px"><td>Hoher Schutzbedarf<br>Ihrer vertraulichen Daten</td><td>Höchster Schutzbedarf<br>Ihrer vertraulichen Daten</td><td class="top">Der allerhöchste Schutzbedarf<br>Ihrer vertraulichen Daten</td></tr>
  </table>
  <div class="crown"><svg width="9" height="7" viewBox="0 0 9 7"><path d="M0 1l2 2 2.5-3L7 3l2-2v5H0z" fill="#fff"/></svg></div>
</section>

<div class="tile products">
  <h2>PRODUKTE</h2>
  <p>Donec quam felis, ultricies nec, pellentesque eu, pretium quis, sem. Nulla consequat massa quis enim. Donec pede justo, fringilla vel, aliquet nec, vulputate eget, arcu. In enim justo, rhoncus ut.</p>
  <div class="more">Zum Onlineshop</div>
</div>
<div class="tile box-photo" role="img" aria-label="Foto eines Aluminium-Sicherheitsbehälters mit Einwurfschlitz"></div>
<div class="tile seal" role="img" aria-label="Siegel für DSGVO-konforme Vernichtung"><span class="badge"></span></div>

<section class="tile offers">
  <h2>AKTUELLE ANGEBOTE IN UNSEREM ONLINESHOP</h2>
  <div class="card" style="left:15px"><div class="shot" role="img" aria-label="Produktfoto Sicherheitsbehälter"></div><h4>Musterprodukt</h4><div class="price">1.350,00 EUR</div><span class="btn">Mehr erfahren</span></div>
  <div class="card" style="left:122px"><div class="shot" role="img" aria-label="Produktfoto Sicherheitsbehälter"></div><h4>Musterprodukt</h4><div class="price">1.350,00 EUR</div><span class="btn">Mehr erfahren</span></div>
  <div class="card" style="left:229px"><div class="shot" role="img" aria-label="Produktfoto Sicherheitsbehälter"></div><h4>Musterprodukt</h4><div class="price">1.350,00 EUR</div><span class="btn">Mehr erfahren</span></div>
  <div class="card hover" style="left:336px"><div class="shot" role="img" aria-label="Produktfoto Sicherheitsbehälter"></div><h4>Musterprodukt</h4><div class="price">1.350,00 EUR</div><span class="btn">Mehr erfahren</span></div>
  <div class="dots"><i></i><i></i><i></i><i></i><i></i></div>
</section>

<a class="abs cta" style="left:236px">ONLINESHOP</a>
<a class="abs cta contact" style="left:371px">KONTAKT</a>

<svg class="abs up" width="12" height="7" viewBox="0 0 12 7"><path d="M1 6l5-4 5 4" stroke="#9dcfc8" stroke-width="2" fill="none"/></svg>
<div class="abs foot-logo"><span>WENZLICK</span><span class="dot"></span></div>
<span class="abs foot-mark"></span>
<div class="abs foot-legal">Impressum . Datenschutz . AGBs<br>Aktenvernichtungs-AGBs . <span>© 2023 Wenzlick + Falkner GmbH</span></div>
</body>
</html>
```